DunePrince.Com Website Design

We need a logo with website designed for the domain duneprince.com. This is a domain that will be a tribute domain for the ruler of Saudi Arabia. For reference you can see how emirkhalidon.com looks and do something similar. The site will need to be easily updateable. We will be adding news and content regularly so it will need to be a very content friendly site. We may even use word-press as the site management tool. We've uploaded the site map in the pdf that's attached along with some images that you can use for the site. Design needs to be per the sitemap. Please feel free to edit the images I've uploaded also use stock images if required.

Industry/Entity Type

Domain

Number of Pages Required

5+ page

Requirements
Must have
• Design has to be per the sitemap attached.

```html
<!DOCTYPE html>
<html lang="en">
<head>
<meta charset="utf-8">
<title>DunePrince.Com</title>
<link href="https://fonts.googleapis.com/css2?family=Barlow:ital,wght@0,400;0,500;0,600;1,400&family=Bebas+Neue&family=Open+Sans:ital,wght@0,400;0,600;1,400;1,600&display=swap" rel="stylesheet">
<style>
:root{
  --olive:#bdbb30;
  --olive-dark:#a9a725;
  --ink:#1f1f1f;
  --nav:#2b2b2b;
  --page:#f5f5f2;
  --feed:#ececea;
  --white:#ffffff;
  --grey:#8a8a8a;
}
*{box-sizing:border-box;margin:0;padding:0}
html,body{width:1200px;height:2308px;overflow:hidden;background:var(--white)}
body{font-family:"Open Sans",Arial,sans-serif;color:var(--ink)}
.canvas{position:relative;width:1200px;height:2308px;overflow:hidden;background:var(--page)}
.abs{position:absolute}
.photo{position:absolute}

/* header */
.site-header{left:0;top:0;width:1200px;height:78px;background:var(--white)}
.brand{left:120px;top:22px;font-family:"Barlow",sans-serif;font-weight:500;font-size:19px;color:var(--olive);letter-spacing:.5px}
.brand-dot{display:inline-block;width:14px;height:14px;border-radius:50%;background:var(--olive);margin-right:8px;vertical-align:-1px}
.lang{left:716px;top:25px;font-size:13px;color:var(--olive)}
.divider{top:26px;width:1px;height:16px;background:#d8d8d8}
.social{top:26px;width:18px;height:18px;border-radius:50%;background:#4a4a4a}
.search{left:901px;top:18px;width:179px;height:31px;border-radius:16px;background:var(--olive);color:#fff;font-size:12px;padding:8px 0 0 18px}
.search svg{position:absolute;right:14px;top:6px}

/* nav */
.main-nav{left:0;top:78px;width:1200px;height:50px;background:var(--nav)}
.nav-home{left:120px;top:0;width:62px;height:50px;background:var(--olive)}
.nav-home svg{position:absolute;left:21px;top:15px}
.nav-item{top:16px;font-family:"Barlow",sans-serif;font-size:15px;color:#e8e8e8;letter-spacing:.5px}
.nav-item.has-menu::after{content:"";display:inline-block;margin-left:8px;border:4px solid transparent;border-top:5px solid var(--olive);vertical-align:-1px}

/* hero */
.hero{left:0;top:128px;width:1200px;height:527px;background:linear-gradient(90deg,#c89a6a 0%,#e2b88b 22%,#f1e4d6 45%,#e9c79e 70%,#c79a62 100%)}
.ticker{left:0;top:531px;width:1200px;height:124px;background:rgba(20,20,20,.82)}
.ticker-label{left:0;top:531px;width:270px;height:124px}
.ticker-title{left:122px;top:558px;font-family:"Barlow",sans-serif;font-weight:600;font-size:28px;line-height:32px;color:#fff;letter-spacing:1px}
.tick-thumb{top:569px;width:94px;height:59px;border:2px solid var(--olive);background:linear-gradient(135deg,#d9c7a4,#9d8a6a)}
.tick-text{top:572px;width:175px;font-family:"Barlow",sans-serif;font-size:13px;line-height:16px;color:#fff}
.tick-date{display:block;font-family:"Open Sans",sans-serif;font-size:10px;margin-top:3px;color:#ddd;white-space:nowrap}
.tick-text.last{width:116px}
.tick-text.last .tick-date{letter-spacing:-.4px}
.tick-arrow{left:1097px;width:26px;height:22px;background:var(--olive)}
.tick-arrow svg{position:absolute;left:8px;top:5px}

/* row one */
.feature-card{left:120px;top:679px;width:291px;height:388px;background:var(--olive)}
.feature-card .photo{left:9px;top:9px;width:274px;height:268px;background:linear-gradient(160deg,#e8e4dc,#8c7f6a 60%,#2e2a26)}
.round-arrow{top:20px;width:32px;height:32px;border-radius:50%;background:#fff}
.round-arrow svg{position:absolute;left:10px;top:9px}
.feature-title{left:9px;top:287px;font-family:"Barlow",sans-serif;font-weight:500;font-size:16px;color:var(--ink)}
.feature-date{left:9px;top:309px;font-size:11px;color:var(--ink)}
.feature-copy{left:9px;top:326px;width:270px;font-size:11px;line-height:15px;color:#fff}

.story{left:420px;top:679px;width:473px;height:388px;background:linear-gradient(180deg,#cbd2cf 0%,#d8c9b7 50%,#8d6f62 100%)}
.story-band{left:0;top:237px;width:473px;height:77px;background:rgba(30,30,30,.45)}
.story-title{left:0;top:252px;width:473px;text-align:center;font-family:"Bebas Neue",sans-serif;font-size:46px;color:#fff;letter-spacing:1px}

.newsletter{left:901px;top:679px;width:179px;height:91px;background:#000}
.newsletter h3{position:absolute;left:7px;top:8px;font-family:"Barlow",sans-serif;font-weight:500;font-size:17px;color:#fff}
.email{left:7px;top:34px;width:163px;height:23px;border-radius:12px;background:#fff;font-size:9px;color:#777;padding:5px 0 0 11px}
.email svg{position:absolute;right:10px;top:7px}
.subscribe{left:77px;top:62px;width:93px;height:17px;border-radius:9px;background:var(--olive);font-family:"Barlow",sans-serif;font-weight:600;font-size:11px;color:#222;text-align:center;line-height:17px}

.topics{left:901px;top:778px;width:179px;height:143px;background:linear-gradient(180deg,#c8c2b6 0%,#6d6a62 55%,#2c2a27 100%)}
.topics h4{position:absolute;left:7px;top:80px;font-family:"Barlow",sans-serif;font-weight:600;font-size:13px;color:#fff}
.topics p{position:absolute;left:7px;top:97px;width:165px;font-size:11px;line-height:13px;color:#fff}

.quotes{left:901px;top:930px;width:179px;height:137px;background:var(--olive);overflow:hidden}
.quotes h4{position:absolute;left:7px;top:8px;font-family:"Barlow",sans-serif;font-weight:600;font-size:16px;color:#fff}
.quotes .rule{left:0;top:36px;width:179px;height:1px;background:rgba(255,255,255,.7)}
.quotes p{position:absolute;left:7px;top:44px;width:160px;font-style:italic;font-size:11px;line-height:15px;color:#fff;z-index:1}
.quote-mark{right:6px;bottom:-60px;font-family:"Barlow",sans-serif;font-weight:600;font-size:120px;color:rgba(0,0,0,.12);line-height:1}

/* row two */
.showcase{left:120px;top:1080px;width:550px;height:452px;background:var(--olive)}
.showcase .photo{left:9px;top:9px;width:533px;height:272px;background:linear-gradient(90deg,#3f5a3a 0%,#6a4b2b 25%,#d7d1c4 50%,#5c4224 75%,#2f3b5a 100%)}
.showcase h2{position:absolute;left:9px;top:291px;width:500px;font-family:"Barlow",sans-serif;font-weight:500;font-size:27px;line-height:31px;color:var(--ink)}
.showcase p{position:absolute;left:9px;top:363px;width:528px;font-size:13px;line-height:18px;color:#fff}

.projects{left:682px;top:1080px;width:398px;height:177px;background:#000}
.projects .photo{left:9px;top:9px;width:380px;height:158px;background:linear-gradient(150deg,#3e3528,#a08a6a 45%,#e9e4d8 70%,#6a5a48)}
.projects-title{left:15px;top:128px;font-family:"Barlow",sans-serif;font-weight:600;font-size:17px;color:#fff}
.projects-title::after{content:"";position:absolute;left:0;bottom:-5px;width:48px;height:3px;background:var(--olive)}
.mini-arrows{left:357px;top:131px}

.social-feed{left:682px;top:1269px;width:398px;height:263px;background:var(--feed);text-align:center}
.social-feed h3{position:absolute;left:0;top:24px;width:398px;font-family:"Barlow",sans-serif;font-weight:500;font-size:26px;color:var(--ink)}
.feed-rule{left:169px;top:61px;width:60px;height:3px;background:var(--olive)}
.feed-dot{left:190px;top:76px;width:18px;height:18px;border-radius:50%;background:#4aa3df}
.social-feed p{position:absolute;left:20px;top:101px;width:358px;font-style:italic;font-size:12px;line-height:17px;color:#777}
.feed-by{left:0;top:172px;width:398px;font-style:italic;font-weight:600;font-size:11px;color:#111}
.feed-by span{color:var(--olive)}
.avatar{left:176px;top:200px;width:46px;height:46px;border-radius:50%;background:linear-gradient(180deg,#d65a78,#c9a08a);border:2px solid #fff}

/* video */
.video{left:120px;top:1548px;width:960px;height:359px;background:linear-gradient(90deg,#9c7350 0%,#c58f6a 30%,#6a4a30 60%,#4a3322 100%)}
.play{left:419px;top:128px;width:123px;height:123px;border-radius:50%;background:rgba(255,255,255,.35)}
.play svg{position:absolute;left:45px;top:37px}

/* footer */
.site-footer{left:0;top:1948px;width:1200px;height:316px;background:#0d0d0d}
.foot-col{position:absolute;top:0;font-size:14px;line-height:20px;color:#fff}
.foot-col h4{position:absolute;left:0;white-space:nowrap;font-family:"Barlow",sans-serif;font-weight:500;font-size:21px;color:var(--olive);letter-spacing:.5px}
.foot-col .ln{position:absolute;left:0;white-space:nowrap}
.foot-col .hl{color:var(--olive)}
.foot-col.menu .ln{font-family:"Barlow",sans-serif;font-weight:500;font-size:15px}
.bottom-bar{left:0;top:2264px;width:1200px;height:44px;background:var(--olive);font-size:11px;color:#222}
.bottom-bar .copy{position:absolute;left:120px;top:14px}
.bottom-bar .legal{position:absolute;right:120px;top:14px}
</style>
</head>
<body>
<div class="canvas">

  <header class="site-header abs">
    <div class="brand abs"><span class="brand-dot"></span>H.H. Khalid bin Faris Al Nuri</div>
    <span class="divider abs" style="left:705px"></span>
    <span class="lang abs">عربي</span>
    <span class="divider abs" style="left:756px"></span>
    <span class="social abs" style="left:768px" aria-label="Social link one"></span>
    <span class="divider abs" style="left:797px"></span>
    <span class="social abs" style="left:808px" aria-label="Social link two"></span>
    <span class="divider abs" style="left:837px"></span>
    <span class="social abs" style="left:849px" aria-label="Social link three"></span>
    <div class="search abs">Search
      <svg width="20" height="20" viewBox="0 0 20 20"><circle cx="8" cy="8" r="6" fill="none" stroke="#fff" stroke-width="2.4"/><line x1="12.5" y1="12.5" x2="18" y2="18" stroke="#fff" stroke-width="2.6" stroke-linecap="round"/></svg>
    </div>
  </header>

  <nav class="main-nav abs">
    <div class="nav-home abs"><svg width="20" height="18" viewBox="0 0 20 18"><path d="M10 1 1 9h3v8h5v-5h2v5h5V9h3z" fill="none" stroke="#fff" stroke-width="1.8" stroke-linejoin="round"/></svg></div>
    <span class="nav-item abs" style="left:211px">Home</span>
    <span class="nav-item has-menu abs" style="left:296px">News</span>
    <span class="nav-item has-menu abs" style="left:382px">About</span>
    <span class="nav-item has-menu abs" style="left:470px">Career</span>
    <span class="nav-item has-menu abs" style="left:571px">Foundations and Activities</span>
    <span class="nav-item has-menu abs" style="left:804px">Media</span>
  </nav>

  <div class="hero abs" role="img" aria-label="Portrait of His Highness in traditional red and white headdress before a carved gold wall and flag"></div>

  <section class="ticker abs"></section>
  <svg class="ticker-label abs" width="270" height="124" viewBox="0 0 270 124"><polygon points="0,0 237,0 270,62 237,124 0,124" fill="var(--olive)"/></svg>
  <div class="ticker-title abs">News<br>Updates</div>

  <div class="tick-thumb abs" style="left:285px" role="img" aria-label="News photo"></div>
  <div class="tick-text abs" style="left:388px">Dune Prince-H.H. Khalid bin Faris Al Nuri<span class="tick-date">Sunday 16 October 2016 10:00 AM</span></div>
  <div class="tick-thumb abs" style="left:579px" role="img" aria-label="News photo"></div>
  <div class="tick-text abs" style="left:681px">Dune Prince-H.H. Khalid bin Faris Al Nuri<span class="tick-date">Sunday 16 October 2016 10:00 AM</span></div>
  <div class="tick-thumb abs" style="left:875px" role="img" aria-label="News photo"></div>
  <div class="tick-text last abs" style="left:978px">Dune Prince-H.H.<br>bin Faris Al Nuri<span class="tick-date">Sunday 16 October 2016</span></div>
  <div class="tick-arrow abs" style="top:570px"><svg width="10" height="12" viewBox="0 0 10 12"><path d="M2 1l6 5-6 5" fill="none" stroke="#fff" stroke-width="2"/></svg></div>
  <div class="tick-arrow abs" style="top:597px"><svg width="10" height="12" viewBox="0 0 10 12"><path d="M8 1 2 6l6 5" fill="none" stroke="#fff" stroke-width="2"/></svg></div>

  <article class="feature-card abs">
    <div class="photo" role="img" aria-label="His Highness seated at a formal meeting"></div>
    <span class="round-arrow abs" style="left:206px"><svg width="12" height="14" viewBox="0 0 12 14"><path d="M9 1 3 7l6 6" fill="none" stroke="#333" stroke-width="2"/></svg></span>
    <span class="round-arrow abs" style="left:243px"><svg width="12" height="14" viewBox="0 0 12 14"><path d="M3 1l6 6-6 6" fill="none" stroke="#333" stroke-width="2"/></svg></span>
    <div class="feature-title abs">Sheikh Khalid receives at Al Rimal</div>
    <div class="feature-date abs">Thursday December 15 2016</div>
    <p class="feature-copy abs">Lorem ipsum dolor sit amet, consectetuer adipiscing elit, sed diam nonummy nibh euismod tincidunt ut laoreet dolore magna aliquam erat volutpat.</p>
  </article>

  <article class="story abs" role="img" aria-label="Close portrait of His Highness smiling">
    <div class="story-band abs"></div>
    <div class="story-title abs">Story of the Week</div>
  </article>

  <aside class="newsletter abs">
    <h3>Newsletter Signup</h3>
    <div class="email abs">Enter your email...
      <svg width="13" height="9" viewBox="0 0 13 9"><rect width="13" height="9" fill="var(--olive)"/><path d="M0 0l6.5 5L13 0" fill="none" stroke="#fff" stroke-width="1.2"/></svg>
    </div>
    <div class="subscribe abs">Subscribe</div>
  </aside>

  <aside class="topics abs" role="img" aria-label="Officials seated at a conference">
    <h4>Popular Topics</h4>
    <p>Lorem ipsum dolor sit amet, consectetuer adipiscing.</p>
  </aside>

  <aside class="quotes abs">
    <h4>Quotes by the Prince</h4>
    <div class="rule abs"></div>
    <p>Duis autem vel eum iriure dolor in hendrerit in vulputate velit esse molestie consequat, vel illum dolore blandit prae sent lup tatum</p>
    <span class="quote-mark abs">&rdquo;</span>
  </aside>

  <article class="showcase abs">
    <div class="photo" role="img" aria-label="His Highness standing in an office beside a flag"></div>
    <h2>Showcase of various organizations and projects of Prince Faris</h2>
    <p>Lorem ipsum dolor sit amet, consectetuer adipiscing elit, sed diam nonummy nibh euismod tincidunt ut laoreet dolore magna aliquam erat volutpat. Ut wisi enim ad minim veniam, quis nostrud exerci tation ullamcorper suscipit lobortis nisl ut aliquip ex ea commodo</p>
  </article>

  <article class="projects abs">
    <div class="photo" role="img" aria-label="Dignitaries greeting at an official event"></div>
    <div class="projects-title abs">Projects of Prince Faris</div>
    <svg class="mini-arrows abs" width="24" height="12" viewBox="0 0 24 12"><path d="M7 1 2 6l5 5M17 1l5 5-5 5" fill="none" stroke="#fff" stroke-width="1.5"/></svg>
  </article>

  <section class="social-feed abs">
    <h3>Social Feed</h3>
    <div class="feed-rule abs"></div>
    <span class="feed-dot abs"></span>
    <p>Lorem ipsum dolor sit amet, consectetuer adipiscing elit, sed diam nonummy nibh euismod tincidunt ut laoreet dolore magna aliquam erat volutpat.</p>
    <div class="feed-by abs">Dune Prince - H.H. <span>Khalid bin Faris Al Nuri</span></div>
    <div class="avatar abs" role="img" aria-label="Profile photo"></div>
  </section>

  <section class="video abs" role="img" aria-label="Video still of His Highness in profile">
    <div class="play abs"><svg width="44" height="50" viewBox="0 0 44 50"><polygon points="0,0 44,25 0,50" fill="#2a2a2a"/></svg></div>
  </section>

  <footer class="site-footer abs">
    <div class="foot-col" style="left:120px">
      <h4 style="top:30px">INFORMATION</h4>
      <span class="ln hl" style="top:80px">Prince Faris bin Nuri</span>
      <span class="ln" style="top:106px">(Introduction to the reasons for doing this project)</span>
      <span class="ln" style="top:132px">(Short info on family members of the Royal Family)</span>
      <span class="ln hl" style="top:179px">Sheikh Khalid</span>
      <span class="ln" style="top:203px">(Introduction to the project)</span>
      <span class="ln" style="top:230px">About Sheikh Khalid</span>
      <span class="ln" style="top:256px">About the Emirate</span>
    </div>
    <div class="foot-col" style="left:510px">
      <h4 style="top:30px">ABOUT US</h4>
      <span class="ln" style="top:80px">(Reasons for doing this project on Prince Faris)</span>
      <span class="ln hl" style="top:113px">Contribution</span>
      <span class="ln" style="top:140px">(Our vision and goal for this website)</span>
      <span class="ln hl" style="top:173px">"The Sheikh"</span>
      <span class="ln hl" style="top:197px">Awards and Achievements</span>
      <span class="ln hl" style="top:223px">Horizon Plan</span>
      <span class="ln hl" style="top:251px">Kingdom of the Dunes</span>
      <span class="ln" style="top:282px">(History and information)</span>
    </div>
    <div class="foot-col menu" style="left:881px">
      <span class="ln" style="top:27px">Quotes</span>
      <span class="ln" style="top:56px">Speeches</span>
      <span class="ln" style="top:85px">Foundations</span>
      <span class="ln" style="top:115px">Thoughts</span>
      <span class="ln" style="top:143px">Interviews</span>
      <span class="ln" style="top:172px">Articles</span>
      <span class="ln" style="top:201px">Gallery</span>
    </div>
  </footer>

  <div class="bottom-bar abs">
    <span class="copy">Copyrights © H.H. Khalid bin Faris Al Nuri all rights reserved</span>
    <span class="legal">Privacy Policy &nbsp;-&nbsp; Terms &amp; Conditons</span>
  </div>

</div>
</body>
</html>
```